Creative BLOG HEADER and NEWSLETTER OPTIN for a Training Consultant

What I do
I am a training consultant, mentor and coach specialised in training trainers to train more effectively by showing them how to hack the way people learn. I also help training consultant to commercialise their intellectual property and work with entrepreneurs, small business owners and professionals changing careers who need to gain clarity and apply strategic thinking to their next steps.
See more on http://marcelvintor.com.au/about-marcel/ .
My background is in Business, Marketing, Innovation capability and Learning & Development.
Communicate differentiation:
I have a minimalist blog that I am happy with, but I need a HEADER and an OPT-IN FORM designed to help me communicate my unique selling proposition and differentiate myself from old-school training consultants.
The programs I offer are different because they are outcome or result driven with emphasis on applied creativity and problem solving. While traditional training consultants focus on knowledge transfer, I focus on facilitating tangible outcomes.
I focus a lot on "Unpacking my clients brains" before offering advice. When I start to work with a new client, be it a coaching or training client, I use a A5 blank sheet as a canvas to make the process of "unpacking the client's brain" more visual and clearly define the desired outcomes.
I rely strongly in strategy and a hacker's mindset to generate outcomes from client.
Header requirement:
- I'd like my blog to communicate my process of debriefing new clients ("unpacking brains")
- I'd like the design to have a 'sketchy' feel
- I'd like a design that communicates playfulness, applied creativity, a hackers mindset, strategy, results orientation and street smart learning.
- Social Media ICONS and contact info on top
Visual references:
See a banner I had designed attached. It would be nice to follow the same kind of concept.
Other visual references:
http://stockvale.net/item/3d-metal-human-brain-inside-pencil-light-bulb-with-business-stra/4182056
http://stockvale.net/item/hannd-drawing-light-bulb-and-creative-word-design-as-concept/3516279
Optin form:
- A newsletter opt-in form to be uploaded on the sidebar (i use postwren) with headline: "Tinkering Shift Monthly Newsletter" and a call to action.
I do want to use my photo, but not sure how to go about that. Accepting suggestions.
Best photo I have attached.
See reference for USER EXPERIENCE http://fairpane.org/
Updates
Project Deadline Extended
Reason: Received one great design that didn't fully fit the briefing. Trying to collaborate with designer to solve the issue.
Still accepting entries though.
Cheers,
Marcle

```html
<!DOCTYPE html>
<html lang="en">
<head>
<meta charset="utf-8">
<title>Lumora Training and Development</title>
<link href="https://fonts.googleapis.com/css2?family=Oswald:wght@400;500&family=Lato:wght@400;700&display=swap" rel="stylesheet">
<style>
:root{
  --blue:#1b5592;
  --blue-dark:#0d3f78;
  --nav-top:#1a5fa3;
  --nav-bottom:#0b3d78;
  --green:#5f9c3c;
  --green-dark:#3f7a25;
  --ink:#333;
  --text:#3d3d3d;
  --rule:#c9c9c9;
  --header-bg:#ececec;
  --section-bg:#ebebeb;
  --footer-bg:#353535;
  --footer-text:#e6e6e6;
}
*{margin:0;padding:0;box-sizing:border-box}
html,body{width:1200px;height:1179px;overflow:hidden}
body{font-family:'Lato',sans-serif;color:var(--text);background:#fff;position:relative}
.wrap{width:856px;margin-left:172px;position:relative}

/* header */
.site-header{height:122px;background:linear-gradient(#f1f1f1,#e4e4e4);position:relative}
.brand{position:absolute;left:172px;top:22px}
.brand-name{font-family:'Oswald',sans-serif;font-weight:500;font-size:58px;line-height:60px;color:var(--blue);letter-spacing:2px}
.brand-tag{font-family:'Lato',sans-serif;font-size:14.5px;color:#333;letter-spacing:.3px;margin-top:2px}
.social{position:absolute;right:172px;top:9px;display:flex;gap:6px;list-style:none}
.social li{width:27px;height:27px;border-radius:50%}
.social .s1{background:#3b5a98}.social .s2{background:#2ea9e1}.social .s3{background:#1c83b8}.social .s4{background:#f08a1c}
.enquiry{position:absolute;right:172px;top:54px;width:198px;height:49px;background:#fff;border:1px solid #cfcfcf;display:flex;align-items:center;padding-left:8px}
.enquiry svg{flex:none}
.enquiry-text{margin-left:6px}
.enquiry-label{font-size:15px;color:#333;line-height:16px}
.enquiry-phone{font-family:'Oswald',sans-serif;font-weight:500;font-size:21px;color:var(--blue);line-height:24px}

/* nav */
.main-nav{height:48px;background:linear-gradient(var(--nav-top),var(--nav-bottom));border-top:2px solid #0d3a6b}
.main-nav ul{list-style:none;display:flex;height:46px;margin-left:172px}
.main-nav li{font-family:'Oswald',sans-serif;font-size:19px;color:#fff;display:flex;align-items:center;justify-content:center;border-right:1px solid #083463;height:46px}
.main-nav li:last-child{border-right:none}
.main-nav .current{background:linear-gradient(var(--green),var(--green-dark))}
.nav-home{width:126px}.nav-blog{width:138px}.nav-about{width:248px}.nav-work{width:214px}.nav-contact{width:130px}

/* hero */
.hero{height:469px;background:radial-gradient(ellipse at 50% 55%,#c98070 0,#d9cfc0 28%,#ddd8cb 60%,#d2cdc0 100%)}

/* about */
.about{height:339px;padding-top:28px}
.section-title{font-family:'Oswald',sans-serif;font-weight:400;font-size:35px;color:var(--ink);display:flex;align-items:center;line-height:40px}
.section-title .accent{color:var(--blue);margin-left:8px}
.title-rule{flex:1;height:1px;background:var(--rule);margin-left:10px;position:relative;top:4px}
.title-rule::before{content:"";position:absolute;left:0;top:-4px;width:8px;height:8px;border:1px solid var(--rule);background:#fff}
.about-body{display:flex;margin-top:12px}
.about-text{width:620px;font-size:14px;line-height:22.5px}
.about-text p{margin-bottom:8px}
.profile{margin-left:43px;width:186px;text-align:center}
.profile-photo{width:186px;height:187px;background:linear-gradient(135deg,#a8b37a,#c7a88a 50%,#3a3a3a);border-radius:2px}
.profile-name{font-family:'Oswald',sans-serif;font-size:21px;color:var(--blue);margin-top:8px}

/* newsletter */
.newsletter{height:150px;background:var(--section-bg);text-align:center;padding-top:16px}
.newsletter-title{font-family:'Oswald',sans-serif;font-size:34px;color:var(--ink);display:flex;justify-content:center;align-items:center;gap:16px;line-height:40px}
.newsletter-title .accent{color:var(--blue)}
.newsletter-lead{font-size:14px;color:#444;margin-top:8px}
.optin{display:flex;margin:17px 0 0 217px;gap:0}
.field{width:271px;height:29px;background:#fff;border:1px solid #cfcfcf;display:flex;align-items:center;justify-content:space-between;padding:0 8px;font-size:12px;color:#555}
.field + .field{margin-left:28px}
.signup{margin-left:20px;width:158px;height:32px;background:linear-gradient(var(--nav-top),var(--blue-dark));color:#fff;font-family:'Lato',sans-serif;font-weight:700;font-size:17px;border:none;border-bottom:2px solid #082c57;border-radius:2px;margin-top:-1px}

/* footer */
.site-footer{height:51px;background:var(--footer-bg);color:var(--footer-text);font-size:13px;display:flex;align-items:center;padding:0 98px 0 173px;justify-content:space-between}
.footer-nav{list-style:none;display:flex}
.footer-nav li+li::before{content:"::";margin:0 22px;color:#bbb}
</style>
</head>
<body>

<header class="site-header">
  <div class="brand">
    <div class="brand-name">LUMORA</div>
    <div class="brand-tag">TRAINING AND DEVELOPMENT</div>
  </div>
  <ul class="social" aria-label="Social links">
    <li class="s1"></li><li class="s2"></li><li class="s3"></li><li class="s4"></li>
  </ul>
  <div class="enquiry">
    <svg width="40" height="44" viewBox="0 0 40 44" aria-hidden="true">
      <path d="M8 3c-4 2-6 7-3 15 4 10 12 18 22 22 5 2 8 1 10-2l-6-7-6 3c-5-3-9-7-12-13l4-5z" fill="#1b5592"/>
    </svg>
    <div class="enquiry-text">
      <div class="enquiry-label">Call for Enquiry</div>
      <div class="enquiry-phone">(61) 400 555 019</div>
    </div>
  </div>
</header>

<nav class="main-nav">
  <ul>
    <li class="nav-home current">HOME</li>
    <li class="nav-blog">BLOG</li>
    <li class="nav-about">ABOUT THE AUTHOR</li>
    <li class="nav-work">WORK WITH ME</li>
    <li class="nav-contact">CONTACT</li>
  </ul>
</nav>

<section class="hero" role="img" aria-label="Sketchy illustration of a brain wired to gears and icons with the phrases Boost your creativity, Sell your ideas, Learn faster, Do what you love and Change the world"></section>

<section class="about">
  <div class="wrap">
    <h2 class="section-title">About<span class="accent">Marcel Vintor</span><span class="title-rule"></span></h2>
    <div class="about-body">
      <div class="about-text">
        <p>I am a self confessed learning and development freak. A hacker of all things related to optimised learning capacity and things that put us into a state of flow. I’ve been a lifetime students of what makes us tick and I always had an insatiable curiosity for uncovering strategies to make real change happen.</p>
        <p>Lorem ipsum dolor sit amet, consectetuer adipiscing elit, sed diam nonua nibh euismod tincidunt ut laoreet dolore magna aliquam erat volutpat. in Ut wisi enim ad minim veniam, quis nostrud exerci in tation ullamcorpe a suscipit lobortis nisl ut aliquip ex ea commodo consequat. Duis autemipk velipas eum iriure dolor in hendrerit in vulputate velit esse molestie consequ, vel illum dolore eu feugiat.</p>
      </div>
      <div class="profile">
        <div class="profile-photo" role="img" aria-label="Portrait photo of Marcel Vintor outdoors"></div>
        <div class="profile-name">Marcel Vintor</div>
      </div>
    </div>
  </div>
</section>

<section class="newsletter">
  <h2 class="newsletter-title">
    <svg width="38" height="38" viewBox="0 0 38 38" aria-hidden="true">
      <path d="M2 16 19 4l17 12v20H2z" fill="#6a6a6a"/>
      <rect x="9" y="10" width="20" height="14" fill="#fff"/>
      <path d="M15 14h8v-4h-8z M12 15l7 7 7-7z" fill="#6a6a6a"/>
      <path d="M2 16l17 12 17-12v20H2z" fill="#8a8a8a"/>
    </svg>
    <span>Lumora Training <span class="accent">Monthly Newsletter</span></span>
  </h2>
  <p class="newsletter-lead">Leave your email address to receive our monthly newsletter containing the latest news and informationine .</p>
  <form class="optin">
    <div class="field"><span>Your Name</span>
      <svg width="18" height="18" viewBox="0 0 18 18" aria-hidden="true"><circle cx="9" cy="5" r="4" fill="#bbb"/><path d="M1 18c0-6 4-8 8-8s8 2 8 8z" fill="#bbb"/></svg>
    </div>
    <div class="field"><span>Your Email</span>
      <svg width="18" height="14" viewBox="0 0 18 14" aria-hidden="true"><rect x="1" y="1" width="16" height="12" fill="none" stroke="#aaa" stroke-width="1.4"/><path d="M1 1l8 7 8-7" fill="none" stroke="#aaa" stroke-width="1.4"/></svg>
    </div>
    <button type="button" class="signup">SIGN UP NOW</button>
  </form>
</section>

<footer class="site-footer">
  <ul class="footer-nav">
    <li>Home</li><li>Blog</li><li>About The Author</li><li>Work With Me</li><li>Contact</li>
  </ul>
  <div>© 2014 Marcel Vintor.&nbsp; ALL RIGHTS RESERVED.</div>
</footer>

</body>
</html>
```